ultra-minimalist business card

front (black background, matte):

tarik b. hosseny
writer | photographer
get@tarikhosseny.com

back (white background, matte):

a picture speaks a thousand words;
a word draws a thousand pictures.

www.tarikhosseny.com

all text should be small (white or silver - as long as it shows against the black - on the front; black or gray - as long as it shows against the white - on the back).

feel free to get creative in terms of arrangement, alignment, and font type, but remember, the overall style is minimalist, so nothing too fancy, please.

thanks.

```html
<!DOCTYPE html>
<html lang="en">
<head>
<meta charset="utf-8">
<title>Tarik B. Hosseny – Business Card</title>
<link rel="stylesheet" href="https://fonts.googleapis.com/css2?family=Cinzel:wght@700&family=Didact+Gothic&display=swap">
<style>
  :root {
    --backdrop: #e6e4e1;
    --card-black: #1b1c1e;
    --card-white: #ffffff;
    --ink-white: #f4f4f4;
    --ink-silver: #9a9b9d;
    --ink-black: #141414;
    --ink-gray: #6f6f6f;
    --shadow: rgba(0, 0, 0, 0.18);
  }
  * { margin: 0; padding: 0; box-sizing: border-box; }
  html, body {
    width: 1200px;
    height: 1200px;
    overflow: hidden;
    background: var(--backdrop);
  }
  .canvas {
    position: relative;
    width: 1200px;
    height: 1200px;
  }
  .card {
    position: absolute;
    left: 180px;
    width: 840px;
    height: 480px;
    box-shadow: 0 10px 28px var(--shadow);
  }
  .card--front { top: 100px; background: var(--card-black); }
  .card--back  { top: 620px; background: var(--card-white); }

  .name {
    position: absolute;
    font-family: "Cinzel", "Times New Roman", serif;
    font-weight: 700;
    text-transform: uppercase;
    letter-spacing: 0.06em;
    white-space: nowrap;
  }
  .role, .tagline, .contact {
    position: absolute;
    font-family: "Didact Gothic", "Century Gothic", sans-serif;
    white-space: nowrap;
  }

  /* front */
  .card--front .name {
    left: 150px; top: 168px;
    font-size: 40px;
    color: var(--ink-white);
    text-shadow: 1px 1px 0 #5a5a5a;
  }
  .card--front .role {
    left: 232px; top: 228px;
    font-size: 22px;
    color: var(--ink-silver);
    letter-spacing: 0.02em;
  }
  .card--front .contact {
    left: 150px; top: 346px;
    font-size: 26px;
    color: var(--ink-white);
    letter-spacing: 0.01em;
  }

  /* back */
  .card--back .name {
    left: 200px; top: 110px;
    font-size: 48px;
    color: var(--ink-black);
    text-shadow: 1px 1px 0 #bdbdbd;
  }
  .card--back .tagline {
    left: 120px; top: 190px;
    font-size: 19px;
    color: var(--ink-gray);
    letter-spacing: 0.02em;
  }
  .card--back .contact {
    left: 60px; top: 400px;
    font-size: 20px;
    font-weight: 700;
    color: var(--ink-black);
    -webkit-text-stroke: 0.4px var(--ink-black);
  }
</style>
</head>
<body>
  <main class="canvas">
    <section class="card card--front" aria-label="Card front">
      <h1 class="name">tarik b. hosseny</h1>
      <p class="role">writer | photographer</p>
      <p class="contact contact--email">get@tarikhosseny.com</p>
    </section>

    <section class="card card--back" aria-label="Card back">
      <h2 class="name">tarik b. hosseny</h2>
      <p class="tagline">a picture speaks a thousand words; a word draws a thousand pictures.</p>
      <p class="contact contact--web">www.tarikhosseny.com</p>
    </section>
  </main>
</body>
</html>
```